Business Card Design Project

- makeup artist business card

- original and creative

- Elegant design

- Feel free to come out with cool designs but stick to being elegant and attractive

- Design relates to makeup

- includes name, occupation, contact numbers, email, website

- regular size business card

- round corner card

- double sided

- on 1 side it should just have the website name in the center " velvetbrushhue.com "

Industry/Entity Type

Business

Requirements
Must have
• Marla Tobin
Makeup Artist
USA: +1 (213)555-0147
Singapore: +65 90007312
marlatobin@velvetbrushhue.com
www.velvetbrushhue.com
Should not have
• nothing cartoon looking.
Pictures of makeup being grab from the internet.. Examples: eyes or lips.

```html
<!DOCTYPE html>
<html lang="en">
<head>
<meta charset="utf-8">
<title>velvetbrushhue.com – Business Cards</title>
<link rel="stylesheet" href="https://fonts.googleapis.com/css2?family=Arimo:wght@400;700&family=Gelasio:wght@700&display=swap">
<style>
  :root {
    --bg: #f3e7ea;
    --card: #ffffff;
    --plum: #8a2363;
    --pink: #d6428f;
    --pink-soft: #e48abb;
    --ink: #222222;
    --brand: #7e2a5f;
    --title: #f4c9df;
  }
  * { box-sizing: border-box; margin: 0; padding: 0; }
  html, body {
    width: 1200px; height: 951px; overflow: hidden;
    background: var(--bg);
    font-family: "Arimo", Arial, sans-serif;
  }
  .canvas { position: relative; width: 1200px; height: 951px; }

  .card {
    position: absolute;
    width: 560px; height: 320px;
    background: var(--card);
    border-radius: 24px;
    overflow: hidden;
    box-shadow: 0 6px 18px rgba(90, 30, 60, 0.15);
  }

  /* Back side */
  .card--back { left: 90px; top: 110px; }
  .back-domain {
    position: absolute; left: 0; right: 0; top: 146px;
    display: flex; align-items: center; justify-content: center; gap: 14px;
  }
  .domain-text { font-size: 26px; color: var(--pink); letter-spacing: 0.2px; }
  .domain-text .tld { color: var(--ink); }
  .dots { display: flex; align-items: center; gap: 9px; }
  .dots i { display: block; border-radius: 50%; background: var(--pink); }
  .dots i:nth-child(1) { width: 3px; height: 3px; }
  .dots i:nth-child(2) { width: 4px; height: 4px; }
  .dots i:nth-child(3) { width: 5px; height: 5px; }
  .dots i:nth-child(4) { width: 6px; height: 6px; }
  .dots i:nth-child(5) { width: 7px; height: 7px; }
  .dots--right { flex-direction: row-reverse; }

  /* Front side */
  .card--front { left: 550px; top: 520px; }
  .band { position: absolute; inset: 0; width: 560px; height: 320px; }

  .brand {
    position: absolute; left: 30px; top: 60px;
    font-size: 34px; line-height: 40px; font-weight: 400;
    color: var(--brand); white-space: nowrap;
  }

  .contacts {
    position: absolute; left: 30px; top: 196px;
    list-style: none; font-size: 13.5px; line-height: 21px; color: var(--ink);
  }
  .contacts li { display: flex; align-items: center; gap: 8px; }
  .contacts svg { width: 13px; height: 13px; flex: none; }
  .contacts .accent { color: var(--pink); }

  .identity {
    position: absolute; left: 340px; right: 0; top: 238px;
    text-align: center;
  }
  .identity .name {
    font-family: "Gelasio", Georgia, serif; font-weight: 700;
    font-size: 22px; color: #ffffff;
  }
  .identity .role { font-size: 15px; color: var(--title); margin-top: 4px; }
</style>
</head>
<body>
<main class="canvas">

  <section class="card card--back" aria-label="Card back">
    <div class="back-domain">
      <span class="dots"><i></i><i></i><i></i><i></i><i></i></span>
      <span class="domain-text">velvetbrushhue<span class="tld">.com</span></span>
      <span class="dots dots--right"><i></i><i></i><i></i><i></i><i></i></span>
    </div>
  </section>

  <section class="card card--front" aria-label="Card front">
    <svg class="band" viewBox="0 0 560 320" aria-hidden="true">
      <defs>
        <linearGradient id="plumFill" x1="0" y1="0" x2="1" y2="0">
          <stop offset="0" stop-color="#7c1b58"/>
          <stop offset="1" stop-color="#9a2f70"/>
        </linearGradient>
      </defs>
      <path d="M262,0 C312,80 320,220 300,320 L326,320 C344,220 336,80 296,0 Z" fill="var(--pink-soft)"/>
      <path d="M296,0 C336,80 344,220 326,320 L333,320 C351,220 343,80 303,0 Z" fill="#ffffff"/>
      <path d="M303,0 C343,80 351,220 333,320 L560,320 L560,0 Z" fill="url(#plumFill)"/>
    </svg>

    <h1 class="brand">velvet brush hue</h1>

    <ul class="contacts">
      <li>
        <svg viewBox="0 0 14 14"><circle cx="7" cy="7" r="6" fill="none" stroke="var(--pink)" stroke-width="1.4"/><path d="M5 4 Q4 7 6 10" stroke="var(--pink)" stroke-width="1.8" fill="none" stroke-linecap="round"/></svg>
        USA: +1 (213)555-0147
      </li>
      <li>
        <svg viewBox="0 0 14 14"><circle cx="7" cy="7" r="6" fill="none" stroke="var(--pink)" stroke-width="1.4"/><path d="M5 4 Q4 7 6 10" stroke="var(--pink)" stroke-width="1.8" fill="none" stroke-linecap="round"/></svg>
        Singapore: +65 90007312
      </li>
      <li>
        <svg viewBox="0 0 14 14"><rect x="1" y="3" width="12" height="8" rx="1" fill="var(--pink)"/><path d="M1.5 3.5 L7 8 L12.5 3.5" stroke="#ffffff" stroke-width="1" fill="none"/></svg>
        marlatobin@velvetbrushhue.com
      </li>
      <li>
        <svg viewBox="0 0 14 14"><circle cx="7" cy="7" r="6" fill="var(--pink)"/></svg>
        <span>www.<span class="accent">velvetbrushhue</span>.com</span>
      </li>
    </ul>

    <div class="identity">
      <p class="name">Marla Tobin</p>
      <p class="role">Makeup Artist</p>
    </div>
  </section>

</main>
</body>
</html>
```